Bright Arch Group business card

Bright Arch Group is the parent company of Bright Arch Building, Bright Arch Plumbing and Bright Arch Renovating. We require a sophisticated business card that covers all aspects of the building and plumbing space without using told or construction items.

Industry/Entity Type

Construction Company

Contact Information for Business Card

Gareth Pimley
Director
0472915083
gareth@brightarch.com.au
Www.brightarch.com.au

Font styles to use
Serif
Sans Serif

Colors
3176b5
ffce3e
0692cd
34a7d8
fbee3e
faa54b

Requirements
Must have
• Logo on front
• Logo and details on rear.
Nice to have
• Maybe water mark or shadow effect with logo
Should not have
• Tools or any construction associated items

```html
<!DOCTYPE html>
<html lang="en">
<head>
<meta charset="utf-8">
<title>Bright Arch Group – Business Card</title>
<link rel="stylesheet" href="https://fonts.googleapis.com/css2?family=Roboto:wght@400;500&family=Josefin+Sans:wght@300&display=swap">
<style>
  :root {
    --backdrop: #5a3a3e;
    --card-white: #ffffff;
    --card-blue: #2878b6;
    --band-blue: #0b4f9e;
    --accent-orange: #ef7f1a;
    --accent-peach: #f9dfca;
    --ink: #1e1e1e;
  }
  * { box-sizing: border-box; margin: 0; padding: 0; }
  html, body { width: 1200px; height: 1200px; overflow: hidden; }
  body {
    background: var(--backdrop);
    position: relative;
    font-family: "Roboto", sans-serif;
  }
  .card {
    position: absolute;
    width: 732px;
    height: 414px;
    border-radius: 20px;
    overflow: hidden;
    box-shadow: 0 4px 10px rgba(0,0,0,0.35);
  }
  .card--front { left: 236px; top: 154px; background: var(--card-white); }
  .card--back  { left: 234px; top: 634px; background: var(--card-blue); }

  .front-decoration {
    position: absolute;
    left: 0; top: 24px;
    width: 340px; height: 340px;
    background: radial-gradient(ellipse 62% 55% at 35% 48%, rgba(249,223,202,0) 55%, rgba(249,223,202,0.85) 80%, rgba(249,223,202,0) 100%);
  }
  .holder {
    position: absolute;
    left: 22px; top: 144px;
    width: 220px;
    text-align: center;
  }
  .holder__name { color: var(--accent-orange); font-weight: 500; font-size: 29px; line-height: 1.1; }
  .holder__role { color: var(--ink); font-size: 22px; line-height: 1.3; }

  .brand {
    position: absolute;
    text-align: center;
    font-family: "Josefin Sans", sans-serif;
    font-weight: 300;
    text-transform: uppercase;
    white-space: nowrap;
  }
  .brand__dot {
    display: block;
    border-radius: 50%;
    margin: 0 auto;
    background: var(--accent-orange);
  }
  .brand__name { display: block; line-height: 1; }
  .brand__sub { display: block; line-height: 1; }

  .card--front .brand { left: 345px; top: 64px; width: 380px; color: var(--ink); }
  .card--front .brand__dot { width: 24px; height: 24px; margin-bottom: 18px; }
  .card--front .brand__name { font-size: 32px; letter-spacing: 6px; padding-left: 6px; }
  .card--front .brand__sub { font-size: 22px; letter-spacing: 16px; padding-left: 16px; margin-top: 8px; }

  .card--back .brand { left: 166px; top: 72px; width: 400px; color: #ffffff; }
  .card--back .brand__dot { width: 28px; height: 28px; margin-bottom: 20px; }
  .card--back .brand__name { font-size: 38px; letter-spacing: 8px; padding-left: 8px; }
  .card--back .brand__sub { font-size: 26px; letter-spacing: 21px; padding-left: 21px; margin-top: 10px; }

  .contacts { position: absolute; left: 372px; top: 274px; list-style: none; }
  .contacts li { display: flex; align-items: center; height: 28px; font-size: 21px; color: var(--ink); }
  .contacts svg { width: 22px; height: 22px; margin-right: 12px; flex: none; }

  .back-decoration {
    position: absolute;
    left: 0; bottom: 0;
    width: 100%; height: 230px;
    background: linear-gradient(to bottom, rgba(11,79,158,0) 0%, rgba(11,79,158,0.55) 45%, rgba(11,79,158,0.4) 75%, rgba(11,79,158,0.65) 100%);
  }
</style>
</head>
<body>
  <section class="card card--front">
    <div class="front-decoration" role="img" aria-label="Faint peach brand decoration"></div>
    <div class="holder">
      <p class="holder__name">Gareth Pimley</p>
      <p class="holder__role">Director</p>
    </div>
    <div class="brand">
      <span class="brand__dot"></span>
      <span class="brand__name">Bright Arch</span>
      <span class="brand__sub">Group</span>
    </div>
    <ul class="contacts">
      <li>
        <svg viewBox="0 0 22 22"><rect x="6" y="1.5" width="10" height="19" rx="2" fill="none" stroke="#ef7f1a" stroke-width="2"/><circle cx="11" cy="17" r="1.2" fill="#ef7f1a"/></svg>
        0472915083
      </li>
      <li>
        <svg viewBox="0 0 22 22"><rect x="1" y="4" width="20" height="14" fill="#ef7f1a"/><path d="M1 4 L11 12 L21 4 M1 18 L8 10 M21 18 L14 10" fill="none" stroke="#fff" stroke-width="1.5"/></svg>
        gareth@brightarch.com.au
      </li>
      <li>
        <svg viewBox="0 0 22 22" fill="none" stroke="#ef7f1a" stroke-width="1.5"><circle cx="11" cy="11" r="9.5"/><ellipse cx="11" cy="11" rx="4.5" ry="9.5"/><path d="M1.5 11 H20.5 M3 6 H19 M3 16 H19"/></svg>
        Www.brightarch.com.au
      </li>
    </ul>
  </section>

  <section class="card card--back">
    <div class="back-decoration" role="img" aria-label="Deep blue brand decoration"></div>
    <div class="brand">
      <span class="brand__dot"></span>
      <span class="brand__name">Bright Arch</span>
      <span class="brand__sub">Group</span>
    </div>
  </section>
</body>
</html>
```